Business Card Re-Design for a Lighting Designer

I would like my business card re-designed. It is currently high gloss and they scratch too easily. I don not think the current design lends itself well to a matte finish. I have included the current design for reference along with our company logo.
Check out our website for current branding.
http://www.brenmoorastudio.example

Updates
Some of the top contenders are muslim and it is a holiday for them. I do not want to discriminate and would expect the same courtesy for holidays we celebrate.
Target Market(s)
Interior Designers, Architects
Contact Information for Business Card
Logo - Name, Title, Address, Telephone Number and Extension, Email
Font styles to use
Requirements
Must have
- All the information listed on the current business card. If you use Red, it needs to be the red from our logo.
Nice to have
- Vertical and Horizontal Designs will be entertained.
Should not have
- Requirements for a glossy finish...should not look too corporate since we are a design firm.

```html
<!DOCTYPE html>
<html lang="en">
<head>
<meta charset="utf-8">
<title>Bren Moora Studio – Business Card</title>
<link rel="stylesheet" href="https://fonts.googleapis.com/css2?family=Open+Sans:wght@400;700&display=swap">
<style>
  :root {
    --brand-red: #9a1a1e;
    --paper: #ffffff;
    --ink: #222222;
    --muted: #7a7a7a;
    --backdrop: #ececec;
  }
  * { box-sizing: border-box; margin: 0; padding: 0; }
  html, body {
    width: 1200px; height: 960px; overflow: hidden;
    background: var(--backdrop);
    font-family: "Open Sans", Arial, sans-serif;
  }
  .sheet {
    position: relative; width: 1200px; height: 960px;
    display: flex; align-items: center; justify-content: center; gap: 40px;
  }
  .card {
    position: relative; width: 540px; height: 308px;
    background: var(--paper); overflow: hidden;
    box-shadow: 0 4px 6px rgba(0,0,0,0.35);
  }
  .card-art { position: absolute; inset: 0; width: 100%; height: 100%; }

  /* Brand lockup */
  .brand { position: absolute; color: var(--ink); width: max-content; }
  .brand-mark { width: 30px; height: 30px; background: var(--brand-red); margin-bottom: 10px; }
  .brand-name {
    font-weight: 400; font-size: 25px; line-height: 26px; letter-spacing: -0.5px;
    text-transform: uppercase; color: var(--ink);
  }
  .brand-tagline {
    margin-top: 8px; padding-top: 5px; border-top: 1px solid var(--brand-red);
    font-size: 7.5px; letter-spacing: 0.8px; color: var(--muted); text-transform: uppercase;
  }
  .front .brand { left: 64px; top: 80px; }
  .back .brand { left: 22px; top: 206px; }
  .back .brand-name { font-size: 20px; line-height: 21px; }
  .back .brand-tagline { font-size: 6.5px; letter-spacing: 0.6px; margin-top: 7px; }

  /* Contact block */
  .contact {
    position: absolute; right: 24px; top: 118px;
    text-align: right; color: var(--paper); font-size: 12px; line-height: 18px;
  }
  .contact-name { font-weight: 700; font-size: 18px; line-height: 22px; }
  .contact-title { font-size: 12px; line-height: 16px; }
  .divider { display: block; line-height: 18px; }
  .contact-line { display: flex; justify-content: flex-end; align-items: center; gap: 7px; }
  .icon { width: 10px; height: 10px; flex: none; }
</style>
</head>
<body>
<main class="sheet">

  <!-- Front: contact side -->
  <section class="card front">
    <svg class="card-art" viewBox="0 0 540 308" aria-hidden="true">
      <polygon points="215,0 540,0 540,308 314,308" fill="var(--brand-red)"/>
      <polyline points="222,29 345,69 445,69 540,36" fill="none" stroke="var(--paper)" stroke-width="1.6"/>
    </svg>

    <div class="brand">
      <div class="brand-mark"></div>
      <p class="brand-name">Bren Moora<br>Studio</p>
      <p class="brand-tagline">Lighting for Architecture</p>
    </div>

    <div class="contact">
      <p class="contact-name">ODILE FENWICK</p>
      <p class="contact-title">PRINCIPAL</p>
      <span class="divider">–</span>
      <p class="contact-line">555.014.2290 X 1
        <svg class="icon" viewBox="0 0 10 10"><circle cx="5" cy="5" r="5" fill="#fff"/><rect x="2.5" y="3" width="5" height="4" rx="1" fill="var(--brand-red)"/></svg></p>
      <p class="contact-line">odile@brenmoorastudio.example
        <svg class="icon" viewBox="0 0 10 10"><circle cx="5" cy="5" r="5" fill="#fff"/><rect x="2.3" y="3.2" width="5.4" height="3.6" fill="var(--brand-red)"/></svg></p>
      <p class="contact-line">www.brenmoorastudio.example
        <svg class="icon" viewBox="0 0 10 10"><circle cx="5" cy="5" r="5" fill="#fff"/><circle cx="5" cy="5" r="2.8" fill="none" stroke="var(--brand-red)" stroke-width="1"/></svg></p>
      <span class="divider">–</span>
      <p>210 Harlow Mill Road</p>
      <p>Suite 14 Dunmore, Georgia 30399</p>
    </div>
  </section>

  <!-- Back: brand side -->
  <section class="card back">
    <svg class="card-art" viewBox="0 0 540 308" aria-hidden="true">
      <rect width="540" height="308" fill="var(--brand-red)"/>
      <polygon points="82,0 102,0 190,308 0,308 0,208" fill="var(--paper)"/>
    </svg>

    <div class="brand">
      <p class="brand-name">Bren Moora<br>Studio</p>
      <p class="brand-tagline">Lighting for Architecture</p>
    </div>
  </section>

</main>
</body>
</html>
```